Real Estate Marketing Company Needs 1 Page 8.5x11 Price List Flyer Design

We need a 1 page 8.5in x 11in price list flyer that is intended for drop off at local offices. This is intended to show all the services we offer including pricing to potential new clients. It should be separated into sections for the different services we offer. I'd also like some photos and our Logo on the list to make it look nice so its not all text. Try to incorporate the logo colors in the design.

Industry/Entity Type

Real Estate

Requirements
Must have
• Price List
• Photos
• Logo
• website address

```html
<!DOCTYPE html>
<html lang="en">
<head>
<meta charset="utf-8">
<title>Price List – Open Gate Photography</title>
<link href="https://fonts.googleapis.com/css2?family=Lato:ital,wght@0,300;0,400;0,700;0,900;1,700&family=Roboto+Condensed:ital,wght@1,700&display=swap" rel="stylesheet">
<style>
  :root {
    --red: #a31b20;
    --red-dark: #8c1418;
    --charcoal: #333031;
    --text: #3a3a3a;
    --grey-ring: #d9d9d9;
    --orange: #f06a0f;
    --orange-light: #ff9a3c;
    --white: #ffffff;
  }
  * { margin: 0; padding: 0; box-sizing: border-box; }
  html, body { width: 927px; height: 1200px; overflow: hidden; background: var(--white); }
  body { font-family: "Lato", Arial, sans-serif; color: var(--text); }
  .flyer { position: relative; width: 927px; height: 1200px; overflow: hidden; background: var(--white); }
  .abs { position: absolute; }

  /* hero */
  .hero-photo { left: 0; top: 0; width: 927px; height: 500px;
    background: linear-gradient(180deg, #4f86c6 0%, #8db4de 28%, #c9b79a 48%, #b59c77 62%, #6c7f4a 80%, #8f8a7a 100%); }
  .hero-shape { left: 0; top: 0; }
  .photo-ring { border-radius: 50%; background: var(--white); box-shadow: 0 2px 6px rgba(0,0,0,.25); }
  .photo-ring .inner { position: absolute; inset: 9px; border-radius: 50%; border: 6px solid var(--red); overflow: hidden; }
  .photo-ring .fill { width: 100%; height: 100%; }
  .pool { background: linear-gradient(180deg, #5f8f4a 0%, #7fb06a 40%, #4aa6d8 70%, #c27a8a 100%); }
  .living { background: radial-gradient(circle at 50% 30%, #e8c58a 0%, #a77644 45%, #5c3a22 100%); }

  .badge { left: 360px; top: 325px; width: 206px; height: 206px; border-radius: 50%; background: var(--white); box-shadow: 0 2px 6px rgba(0,0,0,.25); }
  .badge .core { position: absolute; inset: 10px; border-radius: 50%;
    background: radial-gradient(circle at 50% 35%, var(--orange-light) 0%, var(--orange) 55%, #d34f05 100%); }
  .badge-top { left: 360px; top: 380px; width: 206px; text-align: center; color: var(--white); font-weight: 900; font-size: 31px; letter-spacing: .5px; }
  .badge-label { left: 307px; top: 422px; width: 313px; height: 55px; background: var(--charcoal); border: 3px solid #1f1d1e;
    color: var(--white); font-weight: 300; font-size: 33px; letter-spacing: 2px; text-align: center; line-height: 49px; }

  /* section headers */
  .tab { height: 42px; background: var(--charcoal); color: var(--white); font-weight: 700; font-size: 26px; line-height: 44px; padding-left: 34px; }
  .bar { height: 30px; background: var(--red); color: var(--white); font-weight: 700; font-size: 15px; }
  .bar span { position: absolute; top: 6px; }

  .rows { font-size: 14.5px; line-height: 23px; color: var(--text); }
  .rows .col { position: absolute; top: 0; white-space: nowrap; }

  .note { color: var(--red); font-family: "Roboto Condensed", "Arial Narrow", sans-serif; font-style: italic; font-weight: 700; font-size: 14px; line-height: 17px; }

  .gallery-plan { left: 538px; top: 729px; width: 148px; height: 205px; background: var(--white); border: 5px solid #e2e2e2; box-shadow: 0 1px 3px rgba(0,0,0,.2); }
  .gallery-plan .fill { width: 100%; height: 100%; background: linear-gradient(180deg, #f6f3ee, #e4dfd6); }
  .gallery-shot { border: 5px solid #e2e2e2; box-shadow: 0 1px 3px rgba(0,0,0,.2); }
  .gallery-shot .fill { width: 100%; height: 100%; }
  .porch { background: linear-gradient(180deg, #f2f2ee 0%, #b9a07a 45%, #8c6a45 75%, #6f8f4c 100%); }
  .aerial { background: linear-gradient(180deg, #c6d6e6 0%, #8fa9c4 35%, #c98a3a 60%, #7a5a2a 100%); }

  /* footer */
  .footer { left: 0; top: 1085px; width: 927px; height: 115px; background: linear-gradient(180deg, #ffffff 0%, #ececec 100%); }
  .divider { top: 1098px; width: 1px; height: 72px; background: #d2d2d2; }
  .footer-info { left: 33px; top: 1103px; font-size: 14px; line-height: 22px; color: var(--text); }
  .footer-info .web { font-weight: 700; color: var(--charcoal); }
  .footer-info .web b { color: var(--red); }
  .contact-name { left: 448px; top: 1079px; font-size: 22px; font-weight: 700; color: var(--red); }
  .contact-phone { left: 446px; top: 1134px; font-size: 29px; font-weight: 700; color: var(--charcoal); letter-spacing: .5px; }
  .brand-mark { left: 778px; top: 1060px; width: 68px; height: 68px; border-radius: 50%; border: 5px solid var(--charcoal); }
  .brand-name { left: 700px; top: 1134px; width: 224px; text-align: center; font-weight: 700; font-size: 17px; letter-spacing: 1px; color: var(--charcoal); line-height: 20px; }
</style>
</head>
<body>
<div class="flyer">

  <!-- hero -->
  <div class="abs hero-photo" role="img" aria-label="Photograph of a large stone mansion with terrace, pool and lounge chairs under a blue sky"></div>
  <svg class="abs hero-shape" width="927" height="520" viewBox="0 0 927 520" aria-hidden="true">
    <polygon points="0,230 360,395 360,520 0,520" fill="#ffffff"/>
    <polygon points="927,185 566,395 566,520 927,520" fill="#ffffff"/>
    <polygon points="0,230 360,395 360,410 0,248" fill="#e9e9e9"/>
    <polygon points="927,185 566,395 566,410 927,205" fill="#e9e9e9"/>
    <rect x="0" y="500" width="927" height="20" fill="#ffffff"/>
  </svg>

  <div class="abs photo-ring" style="left:64px;top:208px;width:220px;height:220px;">
    <div class="inner"><div class="fill pool" role="img" aria-label="Photograph of a backyard pool with a gazebo and flower gardens"></div></div>
  </div>
  <div class="abs photo-ring" style="left:638px;top:190px;width:220px;height:220px;">
    <div class="inner"><div class="fill living" role="img" aria-label="Photograph of a warm living room with fireplace and chandelier"></div></div>
  </div>

  <div class="abs badge"><div class="core"></div></div>
  <div class="abs badge-top">PRICE LIST</div>
  <div class="abs badge-label">PHOTOGRAPHY</div>

  <!-- package pricing -->
  <div class="abs tab" style="left:0;top:514px;width:322px;">PACKAGE PRICING</div>
  <div class="abs bar" style="left:0;top:556px;width:494px;">
    <span style="left:34px;">Package</span><span style="left:173px;">Photos+Floor(Plan)</span><span style="left:429px;">Price</span>
  </div>
  <div class="abs rows" style="left:0;top:595px;width:494px;height:70px;">
    <div class="col" style="left:33px;">Silver Package<br>Gold Package<br>Platinum Package</div>
    <div class="col" style="left:173px;">15 Photos + Floor Plan (3,500 sqft)<br>25 Photos + Floor Plan (4,500 sqft)<br>35 Photos + Floor Plan (5,500 sqft)</div>
    <div class="col" style="left:430px;">$225<br>$300<br>$375</div>
  </div>

  <!-- floor plans -->
  <div class="abs tab" style="left:538px;top:514px;width:255px;">FLOOR PLANS</div>
  <div class="abs bar" style="left:538px;top:556px;width:389px;">
    <span style="left:36px;">Package</span><span style="left:168px;">Photos(Plan)</span><span style="left:315px;">Price</span>
  </div>
  <div class="abs rows" style="left:538px;top:594px;width:389px;height:70px;">
    <div class="col" style="left:35px;">Floor Plan<br>Floor Plan<br>Floor Plan</div>
    <div class="col" style="left:168px;">3,500 sqft<br>4,500 sqft<br>5,500 sqft</div>
    <div class="col" style="left:314px;">$150<br>$175<br>$200</div>
  </div>
  <div class="abs note" style="left:573px;top:664px;">*$25 per additional 500sqft</div>
  <div class="abs note" style="left:573px;top:686px;width:300px;">**Complex floor plans are priced individually regardless of sqft</div>

  <!-- photography only -->
  <div class="abs tab" style="left:0;top:705px;width:343px;">PHOTOGRAPHY ONLY</div>
  <div class="abs bar" style="left:0;top:747px;width:494px;">
    <span style="left:34px;">Photos+Floor(Plan)</span><span style="left:429px;">Price</span>
  </div>
  <div class="abs rows" style="left:0;top:787px;width:494px;height:70px;">
    <div class="col" style="left:33px;">15 Photos + Floor Plan (3,500 sqft)<br>25 Photos + Floor Plan (4,500 sqft)<br>35 Photos + Floor Plan (5,500 sqft)</div>
    <div class="col" style="left:430px;">$225<br>$300<br>$375</div>
  </div>

  <!-- gallery -->
  <div class="abs gallery-plan"><div class="fill" role="img" aria-label="Sample two-storey floor plan drawing"></div></div>
  <div class="abs gallery-shot" style="left:697px;top:729px;width:196px;height:94px;"><div class="fill porch" role="img" aria-label="Photograph of a covered porch with wicker seating"></div></div>
  <div class="abs gallery-shot" style="left:697px;top:836px;width:196px;height:98px;"><div class="fill aerial" role="img" aria-label="Aerial photograph of autumn hills around a lake"></div></div>

  <!-- additional services -->
  <div class="abs tab" style="left:0;top:901px;width:365px;">ADDITIONAL SERVICES</div>
  <div class="abs bar" style="left:0;top:943px;width:927px;">
    <span style="left:34px;">Package</span><span style="left:333px;">Photos/Vedeo(Plan)</span><span style="left:574px;">Price</span>
  </div>
  <div class="abs rows" style="left:0;top:983px;width:927px;height:105px;line-height:20px;">
    <div class="col" style="left:33px;">Aerial Photos:<br>Aerial Video:<br>Branded Video Tour w/ Aerial Video:<br>Twilight Photos:<br>Luxury Package:</div>
    <div class="col" style="left:333px;">3-6 Photos<br>1-3 min video<br>2-4 min video of property<br>3-6 Photos<br>includes all services listed</div>
    <div class="col" style="left:574px;">$200 ($75 if combined with another package)<br>$375<br>$800-$1300<br>$225<br>$2,000</div>
  </div>

  <!-- footer -->
  <div class="abs footer"></div>
  <div class="abs divider" style="left:335px;"></div>
  <div class="abs divider" style="left:678px;"></div>
  <div class="abs footer-info">
    For more information or to book a shoot<br>please visit our website:<br>
    <span class="web">www.<b>OpenGatePhotography</b>.com</span>
  </div>
  <svg class="abs" style="left:382px;top:1112px;" width="36" height="48" viewBox="0 0 24 32" aria-hidden="true">
    <path d="M6 2 L10 2 L12 9 L9 11 C10 16 12 19 15 21 L17 18 L23 21 L22 26 C21 28 19 29 17 28 C9 25 4 17 3 8 C3 5 4 3 6 2 Z" fill="var(--red)"/>
  </svg>
  <div class="abs contact-name">Dana</div>
  <div class="abs contact-phone">555-014-2297</div>
  <div class="abs brand-mark" aria-hidden="true"></div>
  <div class="abs brand-name">OPEN GATE PHOTOGRAPHY</div>

</div>
</body>
</html>
```